Finance Product Agency Business Card Design

We're an agency that provides products (service contracts, gap insurance, tire and wheel, etc) and support to dealership finance departments. We specialize in training finance producers to maximize their potential and also keep them up to date on the ever changing compliance and legal landscape. I'll attach an image of our logo, excited to see what you all come up with. Would also be interested in discussing our new website design with the winner.

Target Market(s)

auto dealerships

Industry/Entity Type

Business

Contact Information for Business Card

Mark Dolvery
Phone 317.624.5583
Fax 855.472.3308
email Mark.Dolvery@brightlanecoverage.example

Requirements
Must have
• basic contact information
Nice to have
• looking for something professional but modern

```html
<!DOCTYPE html>
<html lang="en">
<head>
<meta charset="utf-8">
<title>Brightlane Coverage – Business Card</title>
<link rel="stylesheet" href="https://fonts.googleapis.com/css2?family=Open+Sans:wght@400;600;700&display=swap">
<style>
  :root {
    --page-bg: #e7e6e4;
    --card-white: #ffffff;
    --card-grey: #d9dadb;
    --card-grey-deep: #b9babc;
    --brand-teal: #3f5d6c;
    --brand-teal-dark: #2c4350;
    --ink: #1c1c1c;
    --faint-mark: rgba(63, 93, 108, 0.07);
  }
  * { box-sizing: border-box; margin: 0; padding: 0; }
  html, body {
    width: 1200px;
    height: 844px;
    overflow: hidden;
    background: var(--page-bg);
    font-family: "Open Sans", Arial, sans-serif;
  }
  .stage {
    position: relative;
    width: 1200px;
    height: 844px;
    display: flex;
    align-items: center;
    justify-content: center;
    gap: 60px;
  }
  .card {
    position: relative;
    width: 500px;
    height: 286px;
    overflow: hidden;
    box-shadow: 0 10px 24px rgba(0, 0, 0, 0.18);
  }

  /* Contact side */
  .card--contact {
    background: linear-gradient(100deg, var(--card-grey) 0%, var(--card-white) 45%, var(--card-white) 70%, var(--card-grey) 100%);
  }
  .card__band {
    position: absolute;
    left: 0;
    right: 0;
    height: 10px;
    background: linear-gradient(90deg, var(--brand-teal-dark), var(--brand-teal));
  }
  .card__band--top { top: 0; }
  .card__band--bottom { bottom: 0; }
  .contact__mark {
    position: absolute;
    left: 150px;
    top: 70px;
    width: 150px;
    height: 150px;
    border-radius: 50%;
    background: var(--faint-mark);
  }
  .contact {
    position: absolute;
    left: 0;
    right: 0;
    top: 62px;
    text-align: center;
    color: var(--ink);
  }
  .contact__name {
    font-size: 17px;
    font-weight: 600;
    color: var(--brand-teal);
    margin-bottom: 38px;
    padding-right: 20px;
  }
  .contact__line {
    display: flex;
    align-items: center;
    justify-content: center;
    gap: 5px;
    font-size: 13.5px;
    line-height: 20px;
  }
  .contact__line--email { margin-top: 16px; }
  .contact__icon {
    width: 11px;
    height: 11px;
    fill: var(--ink);
    flex: none;
  }

  /* Brand side */
  .card--brand {
    background: radial-gradient(ellipse at 50% 40%, var(--card-white) 0%, var(--card-grey) 60%, var(--card-grey-deep) 100%);
  }
  .brand__tab {
    position: absolute;
    width: 14px;
    height: 36px;
    background: linear-gradient(180deg, var(--brand-teal-dark), var(--brand-teal));
  }
  .brand__tab--right { right: 0; top: 38px; }
  .brand__tab--left { left: 0; bottom: 38px; }
  .brand {
    position: absolute;
    inset: 0;
    display: flex;
    align-items: center;
    justify-content: center;
    gap: 14px;
  }
  .brand__dot {
    width: 44px;
    height: 44px;
    border-radius: 50%;
    background: var(--brand-teal);
  }
  .brand__name {
    font-size: 32px;
    font-weight: 700;
    color: var(--brand-teal-dark);
    letter-spacing: 0.5px;
  }
</style>
</head>
<body>
<main class="stage">
  <section class="card card--contact" aria-label="Contact side">
    <div class="card__band card__band--top"></div>
    <div class="contact__mark"></div>
    <div class="contact">
      <p class="contact__name">Mark Dolvery</p>
      <p class="contact__line">
        <svg class="contact__icon" viewBox="0 0 24 24" aria-hidden="true"><path d="M6.6 10.8a15.1 15.1 0 0 0 6.6 6.6l2.2-2.2c.3-.3.7-.4 1-.2 1.1.4 2.3.6 3.6.6.6 0 1 .4 1 1V20c0 .6-.4 1-1 1A17 17 0 0 1 3 4c0-.6.4-1 1-1h3.5c.6 0 1 .4 1 1 0 1.3.2 2.5.6 3.6.1.3 0 .7-.2 1z"/></svg>
        317.624.5583
      </p>
      <p class="contact__line">
        <svg class="contact__icon" viewBox="0 0 24 24" aria-hidden="true"><path d="M6 2h10v5H6zM3 8h18v10h-3v4H6v-4H3zm5 7v5h8v-5z"/></svg>
        855.472.3308
      </p>
      <p class="contact__line contact__line--email">
        <svg class="contact__icon" viewBox="0 0 24 24" aria-hidden="true"><path d="M2 5h20v14H2zm2 2v.5l8 5 8-5V7z"/></svg>
        Mark.Dolvery@brightlanecoverage.example
      </p>
    </div>
    <div class="card__band card__band--bottom"></div>
  </section>

  <section class="card card--brand" aria-label="Brand side">
    <div class="brand__tab brand__tab--right"></div>
    <div class="brand__tab brand__tab--left"></div>
    <div class="brand">
      <span class="brand__dot"></span>
      <span class="brand__name">Brightlane Coverage</span>
    </div>
  </section>
</main>
</body>
</html>
```